Business card design needed for rebranded top-end landscaping business

We need a new business card design, incorporating our logo (colours Green #8dc63f and Grey #8a8c8e) and also some options that include the colour dark navy (eg #000040) as our uniforms are navy with white and grey trim.

We are an innovative landscaping company that maintains high-end gardens for meticulous clients. We pride ourselves on our customer service, our professionalism, and our workmanship.

Our business name needs to be easily read and our branding needs to be bold and memorable, without screaming "tradesman"! We prefer clean lines over lots of fine detail.

The design MUST include:
- Business name ("Brindlemere Gardening")
- Logo (file uploaded)
- Employee name
- Phone number
- Email address
- www.brindlemeregardening.com.au
- Facebook & Instagram logos
- The Turfcraft Guild logo (file uploaded) along with the word "Member"
- Licence "Lic. 871396K"

OPTIONAL inclusions:
- "Creating outdoor spaces for our community to be inspired, refreshed and re-energised"
- "Landscape Maintenance - Irrigation - Arboriculture" (dashes can be replaced with dots or other)
- "Fully qualified, licensed & insured"
- "Residential - Strata - Commercial - Real Estate" (dashes can be replaced with dots or other)

Target Market(s)

High-end professionals and retirees, real estate agents

Industry/Entity Type

Landscaping

Contact Information for Business Card

See Project description

Font styles to use
Sans Serif

Colors

Designer to choose colors to be used in the design.

Requirements
Must have
• Must incorporate our logo, and colours Green #8dc63f and Grey #8a8c8e) from the logo, and the colour DARK NAVY (eg #000040).
• The design MUST include:
• - Business name ("Brindlemere Gardening")
• - Logo (file uploaded)
• - Employee name
• - Phone number
• - Email address
• - www.brindlemeregardening.com.au
• - Facebook & Instagram logos
• - The Turfcraft Guild logo (file uploaded) along with the word "Member"
• - Licence "Lic. 871396K"
Nice to have
• OPTIONAL inclusions:
• - "Creating outdoor spaces for our community to be inspired, refreshed and re-energised"
• - "Landscape Maintenance - Irrigation - Arboriculture" (dashes can be replaced with dots or other)
• - "Fully qualified, licensed & insured"
• - "Residential - Strata - Commercial - Real Estate" (dashes can be replaced with dots or other)

```html
<!DOCTYPE html>
<html lang="en">
<head>
<meta charset="utf-8">
<title>Brindlemere Gardening – Business Card</title>
<link rel="stylesheet" href="https://fonts.googleapis.com/css2?family=Questrial&display=swap">
<style>
  :root {
    --navy: #000040;
    --green: #8dc63f;
    --grey: #8a8c8e;
    --ink-soft: #6d6f71;
    --paper: #f7f7f7;
    --backdrop: #e4e2de;
    --white: #ffffff;
  }
  * { box-sizing: border-box; margin: 0; padding: 0; }
  html, body { width: 1200px; height: 900px; overflow: hidden; }
  body {
    background: var(--backdrop);
    font-family: "Questrial", sans-serif;
    position: relative;
  }
  .card {
    position: absolute;
    left: 240px;
    width: 720px;
    height: 412px;
    box-shadow: 0 6px 18px rgba(0,0,0,0.18);
    overflow: hidden;
  }

  /* ---------- Front face ---------- */
  .card-front { top: 28px; background: var(--paper); }
  .side-band {
    position: absolute; left: 0; top: 0; bottom: 0; width: 84px;
    background: var(--navy);
    display: flex; align-items: center; justify-content: center;
  }
  .side-band span {
    transform: rotate(-90deg);
    white-space: nowrap;
    color: var(--white);
    font-size: 30px;
    letter-spacing: 0.2px;
  }
  .brand-mark {
    position: absolute; right: 36px; top: 26px;
    display: flex; align-items: center; gap: 10px;
  }
  .brand-mark .dot {
    width: 30px; height: 30px; border-radius: 50%;
    background: var(--grey);
  }
  .brand-mark .name { color: var(--green); font-size: 19px; }

  .person { position: absolute; left: 130px; top: 92px; }
  .person .full-name {
    color: var(--green); font-size: 62px; letter-spacing: 3px; line-height: 1;
  }
  .person .role {
    color: var(--grey); font-size: 30px; letter-spacing: 2px;
    margin-left: 66px; margin-top: 4px;
  }

  .contact-list {
    position: absolute; left: 118px; top: 250px;
    border-left: 2px solid var(--grey);
    padding-left: 14px;
    list-style: none;
  }
  .contact-list li {
    display: flex; align-items: center; gap: 10px;
    height: 36px;
    color: var(--ink-soft); font-size: 13px; letter-spacing: 0.4px;
    white-space: nowrap;
  }
  .contact-list svg { width: 22px; height: 22px; fill: var(--green); flex: none; }

  .social-list {
    position: absolute; left: 474px; top: 236px;
    border-left: 2px solid var(--grey);
    padding-left: 14px;
    list-style: none;
  }
  .social-list li {
    display: flex; align-items: center; gap: 10px;
    height: 36px;
    color: var(--ink-soft); font-size: 13px; letter-spacing: 0.4px;
    white-space: nowrap;
  }
  .social-list .ring {
    width: 24px; height: 24px; border-radius: 50%;
    border: 2px solid var(--green); flex: none;
  }
  .social-list .badge {
    width: 24px; height: 24px; background: var(--green); flex: none;
  }
  .social-list .licence { padding-left: 34px; }

  /* ---------- Back face ---------- */
  .card-back { top: 468px; background: var(--navy); color: var(--white); }
  .card-back .brand-mark { right: 40px; top: 40px; gap: 14px; }
  .card-back .brand-mark .dot { width: 54px; height: 54px; background: var(--white); }
  .card-back .brand-mark .name { color: var(--white); font-size: 28px; }

  .pitch-lines {
    position: absolute; left: 56px; top: 140px; right: 48px;
    list-style: none;
  }
  .pitch-lines li {
    font-size: 19px; letter-spacing: 1.3px; line-height: 1.3;
    margin-bottom: 14px;
  }
  .site-url {
    position: absolute; left: 0; right: 0; bottom: 30px;
    text-align: center; font-size: 17px; letter-spacing: 1px;
  }
</style>
</head>
<body>

  <section class="card card-front" aria-label="Business card front">
    <div class="side-band"><span>Brindlemere Gardening</span></div>

    <div class="brand-mark">
      <div class="dot"></div>
      <div class="name">Brindlemere Gardening</div>
    </div>

    <div class="person">
      <div class="full-name">Oliver Hartley</div>
      <div class="role">General Manager</div>
    </div>

    <ul class="contact-list">
      <li>
        <svg viewBox="0 0 24 24" aria-hidden="true"><path d="M6.6 10.8a15.2 15.2 0 0 0 6.6 6.6l2.2-2.2a1 1 0 0 1 1-.25 11.4 11.4 0 0 0 3.6.57 1 1 0 0 1 1 1V20a1 1 0 0 1-1 1A17 17 0 0 1 3 4a1 1 0 0 1 1-1h3.5a1 1 0 0 1 1 1c0 1.25.2 2.45.57 3.57a1 1 0 0 1-.25 1z"/></svg>
        +61 2 9481 3057
      </li>
      <li>
        <svg viewBox="0 0 24 24" aria-hidden="true"><path d="M12 2a7 7 0 0 0-7 7c0 5.2 7 13 7 13s7-7.8 7-13a7 7 0 0 0-7-7zm0 9.5A2.5 2.5 0 1 1 12 6.5a2.5 2.5 0 0 1 0 5z"/></svg>
        Street Name, City, Country
      </li>
      <li>
        <svg viewBox="0 0 24 24" aria-hidden="true"><path d="M2 5h20v14H2z M2 5l10 8 10-8" stroke="#f7f7f7" stroke-width="1.5"/></svg>
        oliver.hartley@brindlemeregardening.com.au
      </li>
      <li>
        <svg viewBox="0 0 24 24" aria-hidden="true"><path d="M4 3l16 7-7 2-2 7z"/></svg>
        www.brindlemeregardening.com.au
      </li>
    </ul>

    <ul class="social-list">
      <li><span class="ring"></span>Brindlemere Gardening</li>
      <li><span class="ring"></span>Brindlemere Gardening</li>
      <li><span class="badge"></span>The Turfcraft Guild Member</li>
      <li class="licence">Lic. 871396K</li>
    </ul>
  </section>

  <section class="card card-back" aria-label="Business card back">
    <div class="brand-mark">
      <div class="dot"></div>
      <div class="name">Brindlemere Gardening</div>
    </div>

    <ul class="pitch-lines">
      <li>"Fully qualified, licensed &amp; insured"</li>
      <li>"Residential . Strata . Commercial . Real Estate"</li>
      <li>"Landscape Maintenance . Irrigation . Arboriculture"</li>
      <li>"Creating outdoor spaces for our community to be inspired,<br>refreshed and re-energised"</li>
    </ul>

    <div class="site-url">www.brindlemeregardening.com.au</div>
  </section>

</body>
</html>
```